Bramblewick Meadow Farm

We have an existing website for our Thoroughbred Breeding and racing farm in The Plains Virginia we would like to improve it Our Web address is www.bramblewickmeadow.example
We also have a facebook page and a twitter account for our Stallion Lanternglow whom we would like to Spotlight on our website. More Pictures and Info Available.
We would also like to work with the designer we choose to create our brochure for our farm. as well as some promotional material for our stallion Lanternglow.
Please see the following competitor website, www.quarvendale.example we like the conservative and classic feel of this site design.
Updates

Reason: We want to give everyone a chance to make some changes we feel there have been some great ideas thus far. Thank you

Reason: Waiting on a few design changes from designers to come in.

Target Market(s)

Thoroughbred Breeders and Trainers

Industry/Entity Type

Conservative

Font styles to use
Sans Serif

Colors
3277b5
85abd2
0555a3
ffffff

Requirements
Must have
• Please see current website @ www.bramblewickmeadow.example

```html
<!DOCTYPE html>
<html lang="en">
<head>
<meta charset="utf-8">
<title>Bramblewick Meadow Farm</title>
<link rel="stylesheet" href="https://fonts.googleapis.com/css2?family=Oswald:wght@300;400;600&display=swap">
<style>
  :root {
    --brand-blue: #0555a3;
    --brand-mid: #3277b5;
    --brand-light: #85abd2;
    --nav-active: #3a9bc9;
    --white: #ffffff;
    --nav-bg: #0c0c0c;
    --arrow-bg: rgba(30, 30, 30, 0.75);
    --social-bg: #2f5f8f;
  }
  * { box-sizing: border-box; margin: 0; padding: 0; }
  html, body { width: 1200px; height: 900px; overflow: hidden; background: var(--white); }
  body { font-family: "Oswald", sans-serif; color: var(--white); }

  .hero {
    position: relative;
    width: 1200px;
    height: 820px;
    overflow: hidden;
  }
  .hero-backdrop {
    position: absolute; inset: 0;
    background:
      linear-gradient(180deg,
        #b9b6ac 0%, #a9aba4 12%,
        #5f7471 22%, #4f6660 30%,
        #7a6a4a 38%, #9a6a3c 46%, #7f6a42 54%,
        #5f6a48 62%, #77783c 72%,
        #7d8a3a 80%, #6f9a3e 88%, #5e8c36 100%);
  }

  .brand-mark {
    position: absolute;
    left: 490px; top: 50px;
    width: 230px; height: 230px;
    border-radius: 50%;
    background: var(--brand-blue);
    display: flex; align-items: center; justify-content: center;
    text-align: center;
    box-shadow: 0 4px 10px rgba(0,0,0,0.35);
  }
  .brand-name {
    font-family: "Oswald", sans-serif;
    font-weight: 400;
    font-size: 30px;
    line-height: 1.15;
    letter-spacing: 1px;
    text-transform: uppercase;
    color: var(--white);
    width: 180px;
  }

  .contact-block {
    position: absolute;
    left: 105px; top: 350px;
    width: 992px;
    text-align: center;
  }
  .phone {
    font-weight: 600;
    font-size: 112px;
    line-height: 130px;
    letter-spacing: -1px;
    text-shadow: 0 2px 6px rgba(0,0,0,0.4);
  }
  .rule { height: 1px; background: rgba(255,255,255,0.85); }
  .address {
    font-weight: 300;
    font-size: 36px;
    line-height: 90px;
    letter-spacing: -0.5px;
    text-shadow: 0 1px 4px rgba(0,0,0,0.45);
  }

  .slide-arrow {
    position: absolute; top: 426px;
    width: 40px; height: 54px;
    background: var(--arrow-bg);
    display: flex; align-items: center; justify-content: center;
  }
  .slide-arrow.prev { left: 14px; border-radius: 0 27px 27px 0; width: 42px; }
  .slide-arrow.next { right: 14px; border-radius: 27px 0 0 27px; width: 42px; }

  .social-links {
    position: absolute; top: 724px; left: 535px;
    display: flex; gap: 17px; list-style: none;
  }
  .social-links li {
    width: 32px; height: 42px; border-radius: 50%;
    background: var(--social-bg);
    box-shadow: 0 2px 4px rgba(0,0,0,0.4);
  }

  .main-nav {
    position: absolute; top: 820px; left: 0;
    width: 1200px; height: 80px;
    background: var(--nav-bg);
  }
  .main-nav ul {
    list-style: none;
    display: flex;
    justify-content: center;
    height: 100%;
    padding-left: 6px;
  }
  .main-nav li {
    display: flex; align-items: center;
    padding: 0 23px;
    font-weight: 300;
    font-size: 25px;
    letter-spacing: -0.5px;
    text-transform: uppercase;
  }
  .main-nav li.is-active { background: var(--nav-active); }
</style>
</head>
<body>
  <header class="hero">
    <div class="hero-backdrop" role="img" aria-label="Autumn landscape of wooded Virginia hills above a farmhouse, vineyard and green pasture"></div>

    <div class="brand-mark">
      <span class="brand-name">Bramblewick Meadow Farm</span>
    </div>

    <div class="slide-arrow prev" aria-label="Previous slide">
      <svg width="14" height="18" viewBox="0 0 14 18"><path d="M10 2 L3 9 L10 16" fill="none" stroke="#fff" stroke-width="3"/></svg>
    </div>
    <div class="slide-arrow next" aria-label="Next slide">
      <svg width="14" height="18" viewBox="0 0 14 18"><path d="M4 2 L11 9 L4 16" fill="none" stroke="#fff" stroke-width="3"/></svg>
    </div>

    <div class="contact-block">
      <p class="phone">(555) 014-2739</p>
      <div class="rule"></div>
      <p class="address">2714 MEADOWRUE LANE, ASHCOMBE, VA 20990</p>
      <div class="rule"></div>
    </div>

    <ul class="social-links">
      <li aria-label="Social profile"></li>
      <li aria-label="Professional profile"></li>
      <li aria-label="Stallion news feed"></li>
    </ul>
  </header>

  <nav class="main-nav">
    <ul>
      <li class="is-active">Home</li>
      <li>About</li>
      <li>Stallions</li>
      <li>Our Facility</li>
      <li>Mares &amp; Foals</li>
      <li>Contact</li>
    </ul>
  </nav>
</body>
</html>
```